Realtor business card

Looking for a business card that will stand out from the rest. My area of expertise is residential real estate and loans.

Industry/Entity Type

Residential

Requirements
Must have
• Marcus Whitley, SFR
Broker
Mortgage Loan Originator
Notary Public
DRE License #07329184
NMLS 581706
Cell 714-552-0718
Fax 888-417-2965
www.marcuswhitleyhomes.example
mw@marcuswhitleyhomes.example

```html
<!DOCTYPE html>
<html lang="en">
<head>
<meta charset="UTF-8">
<title>Marcus Whitley, SFR – Business Card</title>
<link href="https://fonts.googleapis.com/css2?family=Questrial&display=swap" rel="stylesheet">
<style>
  :root {
    --navy: #03168b;
    --orange: #ff8c00;
    --white: #ffffff;
    --peach-deep: #f58a5e;
    --peach-mid: #f9b98a;
    --peach-light: #fde6cf;
  }
  html, body {
    margin: 0;
    padding: 0;
    width: 1200px;
    height: 686px;
    overflow: hidden;
    background: var(--white);
  }
  .card {
    position: relative;
    width: 1200px;
    height: 686px;
    overflow: hidden;
    font-family: "Questrial", "Century Gothic", sans-serif;
  }
  .card__photo {
    position: absolute;
    inset: 0;
    background:
      linear-gradient(160deg, var(--peach-deep) 0%, var(--peach-mid) 35%, var(--peach-light) 60%, var(--peach-mid) 85%, var(--peach-deep) 100%);
  }
  .card__shapes {
    position: absolute;
    inset: 0;
  }
  .identity {
    position: absolute;
    top: 34px;
    right: 40px;
    text-align: right;
  }
  .identity__name {
    margin: 0 0 4px;
    color: var(--orange);
    font-size: 41px;
    font-weight: 400;
    line-height: 1.1;
  }
  .identity__role {
    margin: 0;
    color: var(--white);
    font-size: 34px;
    font-style: italic;
    line-height: 46px;
  }
  .contact {
    position: absolute;
    right: 40px;
    top: 462px;
    text-align: right;
    color: var(--white);
  }
  .contact__line {
    margin: 0;
    line-height: 46px;
    font-size: 36px;
  }
  .contact__label { font-size: 34px; }
  .contact__value--accent { color: var(--orange); }
  .contact__cell .contact__value { font-size: 43px; }
  .contact__fax .contact__value { font-size: 35px; }
  .licenses {
    position: absolute;
    left: 257px;
    top: 584px;
    transform: translateX(-50%);
    text-align: center;
    color: var(--navy);
    font-size: 31px;
    line-height: 40px;
    white-space: nowrap;
  }
  .licenses p { margin: 0; }
</style>
</head>
<body>
  <div class="card">
    <div class="card__photo" role="img" aria-label="Upward view of a glass office tower with an atrium skylight, tinted orange"></div>

    <svg class="card__shapes" width="1200" height="686" viewBox="0 0 1200 686" aria-hidden="true">
      <defs>
        <filter id="edge-shadow" x="-10%" y="-10%" width="120%" height="120%">
          <feGaussianBlur stdDeviation="6"/>
        </filter>
      </defs>
      <path class="shape-orange-band" d="M515,0 Q214,343 530,686 L1200,686 L1200,0 Z" fill="var(--orange)"/>
      <path class="shape-shadow" d="M537,0 Q269,343 549,686 L1200,686 L1200,0 Z" fill="#000" opacity="0.55" filter="url(#edge-shadow)"/>
      <path class="shape-navy-panel" d="M545,0 Q281,343 557,686 L1200,686 L1200,0 Z" fill="var(--navy)"/>
    </svg>

    <header class="identity">
      <h1 class="identity__name">Marcus Whitley, SFR</h1>
      <p class="identity__role">Broker</p>
      <p class="identity__role">Mortgage Loan Originator</p>
      <p class="identity__role">Notary Public</p>
    </header>

    <section class="contact">
      <p class="contact__line contact__cell"><span class="contact__label">Cell </span><span class="contact__value contact__value--accent">714-552-0718</span></p>
      <p class="contact__line contact__fax"><span class="contact__label">Fax </span><span class="contact__value contact__value--accent">888-417-2965</span></p>
      <p class="contact__line">www.marcuswhitleyhomes.example</p>
      <p class="contact__line">mw@marcuswhitleyhomes.example</p>
    </section>

    <section class="licenses">
      <p>DRE License #07329184</p>
      <p>NMLS 581706</p>
    </section>
  </div>
</body>
</html>
```